Upgrade UI for an existing app

I have an app that is already in the appstore, and I have finally get to the point where the app is fairly complete in its user flow and app features.

I would like to take the app to the next level, and completely revamp its look and feel, to give it that flat iOS7 look.

The app can be downloaded at https://apps.brindlemark.net/us/app/velora-kit/id504719386?mt=8

And you can log into the app using the credential below:

plume.vander
password

I am also open to new ideas around UX, but my biggest focus is on getting the UI updated, especially for the setting page, support page, and about page.

Thanks,

Ned
Updates

Majority of the submissions are for iPhone, whereas I was hoping for more iPad redesign.

I think the issue is that, a lot of people didn't download the app from appstore.

I have uploaded two zip files with iPad screenshot.  Please submit a few designs that are based off the existing iPad screenshot.

```html
<!DOCTYPE html>
<html lang="en">
<head>
<meta charset="utf-8">
<title>Questions</title>
<link rel="stylesheet" href="https://fonts.googleapis.com/css2?family=Arimo:wght@400&family=Roboto:wght@300;400&display=swap">
<style>
  :root {
    --chrome: #2d3035;
    --chrome-line: #44484e;
    --teal: #33c9a0;
    --teal-line: #5fd8b6;
    --panel: #e6f9fd;
    --ink: #2b2f33;
    --rule: #8a9296;
    --gap: #2d3035;
    --correct: #3a9540;
    --wrong: #b52020;
    --white: #ffffff;
  }
  * { box-sizing: border-box; margin: 0; padding: 0; }
  html, body { width: 676px; height: 1200px; overflow: hidden; background: var(--panel); }
  .screen { position: relative; width: 676px; height: 1200px; overflow: hidden; font-family: "Arimo", Arial, sans-serif; color: var(--ink); }

  .status-bar { position: absolute; left: 0; top: 0; width: 676px; height: 51px; background: var(--chrome); color: var(--white); font-family: "Roboto", Arial, sans-serif; font-size: 24px; }
  .status-bar .signal { position: absolute; left: 6px; top: 14px; }
  .status-bar .carrier { position: absolute; left: 94px; top: 9px; letter-spacing: 0.5px; }
  .status-bar .wifi { position: absolute; left: 172px; top: 13px; }
  .status-bar .clock { position: absolute; left: 0; width: 676px; top: 9px; text-align: center; font-size: 25px; }
  .status-bar .bt { position: absolute; left: 510px; top: 12px; }
  .status-bar .battery-pct { position: absolute; left: 544px; top: 9px; }
  .status-bar .battery { position: absolute; left: 616px; top: 14px; }

  .nav-bar { position: absolute; left: 0; top: 51px; width: 676px; height: 96px; background: var(--chrome); border-top: 1px solid var(--chrome-line); }
  .nav-bar .back { position: absolute; left: 12px; top: 21px; }
  .nav-bar .title { position: absolute; left: 0; width: 676px; top: 15px; text-align: center; color: var(--white); font-family: "Roboto", Arial, sans-serif; font-weight: 300; font-size: 50px; letter-spacing: 1.5px; }

  .progress-bar { position: absolute; left: 0; top: 148px; width: 676px; height: 81px; background: var(--teal); color: var(--white); }
  .progress-bar .count { position: absolute; left: 0; width: 518px; top: 18px; text-align: center; font-family: "Roboto", Arial, sans-serif; font-weight: 300; font-size: 35px; letter-spacing: 0.5px; }
  .progress-bar .tool { position: absolute; top: 0; height: 81px; border-left: 1px solid var(--teal-line); display: flex; align-items: center; justify-content: center; }
  .progress-bar .comment { left: 518px; width: 79px; }
  .progress-bar .bookmark { left: 597px; width: 79px; }

  .prompt { position: absolute; left: 0; width: 676px; background: var(--panel); padding: 0 10px 0 20px; font-size: 20.8px; line-height: 25.4px; }
  .prompt.scenario { top: 229px; height: 195px; padding-top: 18px; border-bottom: 1px solid var(--rule); }
  .prompt.ask { top: 425px; height: 140px; padding-top: 23px; }

  .separator { position: absolute; left: 0; top: 565px; width: 676px; height: 12px; background: var(--gap); }

  .answers { position: absolute; left: 0; top: 577px; width: 676px; list-style: none; }
  .answer { height: 124px; padding: 31px 10px 0 20px; font-size: 20.8px; line-height: 25.4px; background: var(--panel); border-bottom: 1px solid var(--rule); }
  .answer.correct { background: var(--correct); color: var(--white); border-bottom-color: var(--correct); }
  .answer.wrong { background: var(--wrong); color: var(--white); border-bottom-color: var(--wrong); }
</style>
</head>
<body>
<main class="screen">
  <header class="status-bar">
    <svg class="signal" width="84" height="16" viewBox="0 0 84 16" aria-hidden="true">
      <circle cx="8" cy="8" r="6.5" fill="#fff"/>
      <circle cx="25" cy="8" r="6.5" fill="#fff"/>
      <circle cx="42" cy="8" r="6.5" fill="#fff"/>
      <circle cx="59" cy="8" r="6" fill="none" stroke="#fff" stroke-width="1.2"/>
      <circle cx="76" cy="8" r="6" fill="none" stroke="#fff" stroke-width="1.2"/>
    </svg>
    <span class="carrier">KESTO</span>
    <svg class="wifi" width="26" height="20" viewBox="0 0 26 20" aria-hidden="true">
      <path d="M2 7 A16 16 0 0 1 24 7" fill="none" stroke="#fff" stroke-width="3"/>
      <path d="M6 11 A10 10 0 0 1 20 11" fill="none" stroke="#fff" stroke-width="3"/>
      <path d="M13 19 L9 15 A6 6 0 0 1 17 15 Z" fill="#fff"/>
    </svg>
    <span class="clock">4:21 PM</span>
    <svg class="bt" width="16" height="26" viewBox="0 0 16 26" aria-hidden="true">
      <path d="M2 7 L13 18 L8 23 L8 3 L13 8 L2 19" fill="none" stroke="#9aa0a6" stroke-width="2"/>
    </svg>
    <span class="battery-pct">100%</span>
    <svg class="battery" width="52" height="22" viewBox="0 0 52 22" aria-hidden="true">
      <rect x="1" y="1" width="45" height="20" rx="3" fill="none" stroke="#fff" stroke-width="2"/>
      <rect x="4" y="4" width="39" height="14" rx="1" fill="#fff"/>
      <rect x="47" y="7" width="3" height="8" fill="#fff"/>
    </svg>
  </header>

  <nav class="nav-bar">
    <svg class="back" width="30" height="52" viewBox="0 0 30 52" aria-label="Back" role="img">
      <path d="M26 3 L4 26 L26 49" fill="none" stroke="#fff" stroke-width="4"/>
    </svg>
    <h1 class="title">Questions</h1>
  </nav>

  <section class="progress-bar">
    <div class="count">16 of 125</div>
    <div class="tool comment">
      <svg width="42" height="32" viewBox="0 0 42 32" aria-label="Comments" role="img">
        <ellipse cx="21" cy="12" rx="20" ry="11.5" fill="#fff"/>
        <path d="M9 19 L5 30 L18 22 Z" fill="#fff"/>
      </svg>
    </div>
    <div class="tool bookmark">
      <svg width="28" height="38" viewBox="0 0 28 38" aria-label="Bookmark" role="img">
        <path d="M1 0 H27 V38 L14 25 L1 38 Z" fill="#fff"/>
      </svg>
    </div>
  </section>

  <p class="prompt scenario">The head team physician for a professional basketball team is also their orthopaedic surgeon. A veteran player sustains a knee injury during practice that requires arthroscopic microfracture knee surgery. The player asks the surgeon not to disclose the severity to the team.</p>
  <p class="prompt ask">When discussing the matter with team officials, what would be the most appropriate action for the team physician?</p>

  <div class="separator"></div>

  <ol class="answers">
    <li class="answer correct">A.&nbsp; Discloser relevant information related to injuries sustained while playing with the team.</li>
    <li class="answer">B.&nbsp; Discloser all health matters that may relate to the player’s future athletic participation.</li>
    <li class="answer">C.&nbsp; Refuse to discuss all health matters regarding this player.</li>
    <li class="answer wrong">D.&nbsp; Disclose the procedure performed but not the severity of the injury.</li>
    <li class="answer">D.&nbsp; Disclose only health matters for which the player specifically provides consent.</li>
  </ol>
</main>
</body>
</html>
```